New Template design for Website in Wordpress

We are interested in changing our website look at www.cargolinx.com -We also are very interested in Have it done in Wordpress in which we are understanding the search engines are liking a bit more. The website we would want to try working with on this is www.cargolinx.com. We look forward to seeing the different design ideas please just make sure they are in wordpress! Thanks, Marlen

Reason: need more design idea..... We would still like to use our pictures off our site since we paid for them so keep that in mind as well as we would still want the rotating pictures in the head of the page but not in Flash.

```html
<!DOCTYPE html>
<html lang="en">
<head>
<meta charset="utf-8">
<title>CargoLinx – Home</title>
<link href="https://fonts.googleapis.com/css2?family=Lato:wght@300;400;700&family=Open+Sans:wght@400;600&display=swap" rel="stylesheet">
<style>
:root{
  --blue:#1a73c9;
  --red:#c8161d;
  --ink:#1c1c1c;
  --text:#5e5e5e;
  --muted:#777;
  --grey-bar:#5f5f5f;
  --page:#ececec;
  --panel:#ffffff;
  --news:#f4f4f4;
  --footer:#262626;
  --footer-text:#9a9a9a;
  --green:#4d8a1a;
}
*{box-sizing:border-box;margin:0;padding:0}
html,body{width:960px;height:1200px;overflow:hidden}
body{position:relative;background:var(--page);font-family:"Lato",sans-serif;color:var(--text)}
.abs{position:absolute}

.site-header{left:0;top:0;width:960px;height:76px;background:#fff;border-top:1px solid #444}
.brand{left:90px;top:20px;font-family:"Open Sans",sans-serif;font-size:22px;color:var(--ink);letter-spacing:-.5px;line-height:1}
.brand-tag{left:91px;top:47px;font-size:12.5px;color:var(--blue);font-weight:300;letter-spacing:.2px}
.main-nav a{position:absolute;top:32px;font-family:"Open Sans",sans-serif;font-size:12px;font-weight:600;color:#222;text-decoration:none}
.main-nav a.active{color:var(--blue)}
.btn-reserve{left:756px;top:24px;width:108px;height:27px;background:var(--red);border:1px solid #a00;color:#fff;font-size:11.5px;display:flex;align-items:center;justify-content:center;gap:6px;letter-spacing:.2px}

.hero{left:0;top:76px;width:960px;height:392px;background:linear-gradient(180deg,#b8c6d3 0%,#c9a55a 35%,#b98a3c 55%,#3a3434 80%,#4a6d8a 100%)}
.hero-caption{left:112px;top:126px;width:460px;height:80px;background:rgba(90,90,90,.72)}
.hero-caption h1{position:absolute;left:14px;top:12px;font-family:"Open Sans",sans-serif;font-weight:400;font-size:22px;color:#fff;letter-spacing:-.3px}
.hero-caption p{position:absolute;left:15px;top:46px;font-size:9.5px;color:#fff;letter-spacing:.1px}
.slider-arrow{top:252px;width:34px;height:39px;background:#fff;display:flex;align-items:center;justify-content:center}

.content-panel{left:89px;top:390px;width:798px;height:541px;background:var(--panel);box-shadow:0 1px 2px rgba(0,0,0,.12)}
.service-card{top:416px;width:235px;height:110px}
.service-card .thumb{height:63px}
.service-card .bar{height:47px;background:var(--grey-bar);padding:12px 14px 0}
.service-card h3{font-weight:400;font-size:9.5px;color:#fff;letter-spacing:.1px}
.service-card span{display:block;margin-top:4px;font-size:9px;color:#d8b560}

.section-title{font-size:11px;letter-spacing:.1px}
.rule{height:3px;border-top:1px solid #ddd;border-bottom:1px solid #ddd}
.intro-photo{left:112px;top:591px;width:130px;height:189px;background:linear-gradient(160deg,#c9cfd6 0%,#e8d27a 35%,#f2f2f2 60%,#5d7fa8 100%)}
.intro-copy{left:262px;top:593px;width:350px;font-size:9.6px;line-height:16.5px}
.intro-copy p+p{margin-top:16px}
.cta{left:262px;top:791px;width:350px;font-size:9.8px;line-height:16.5px;color:var(--red);font-weight:700}

.sidebar h4{font-weight:400;font-size:12px;color:var(--red);margin-bottom:3px}
.sidebar ul{list-style:none;font-size:9.2px;line-height:16.5px;color:#555}
.sidebar ul+h4{margin-top:15px}

.newsletter{left:89px;top:847px;width:798px;height:84px;background:var(--news);border-top:1px solid #e2e2e2}
.newsletter label{position:absolute;left:176px;top:28px;font-size:16px;color:#777}
.newsletter .field{position:absolute;left:349px;top:22px;width:176px;height:28px;background:#fff;border:1px solid #dcdcdc;font-size:9.5px;color:#999;padding:7px 9px}
.newsletter .submit{position:absolute;left:543px;top:22px;width:86px;height:28px;background:var(--green);border:1px solid #3b6e10;color:#fff;font-size:11.5px;display:flex;align-items:center;justify-content:center}

.site-footer{left:0;top:963px;width:960px;height:237px;background:var(--footer)}
.site-footer h5{position:absolute;top:34px;font-weight:400;font-size:11.5px;color:#fff;letter-spacing:.1px}
.contact-list{left:112px;top:70px;font-size:8.2px;color:#ddd;line-height:20.5px;list-style:none}
.contact-list li{display:flex;align-items:center;gap:8px;height:20.5px}
.contact-list svg{width:8px;height:10px;flex:none}
.link-col{list-style:none;font-size:8.4px;color:var(--footer-text);line-height:23px}
.link-col li::before{content:"›";margin-right:7px}
.footer-rule{left:112px;top:1141px;width:752px;border-top:1px solid #3a3a3a}
.footer-note{left:112px;top:1156px;font-size:9.2px;color:#8a8a8a;line-height:14.5px}
.social-label{left:723px;top:1161px;font-size:9px;color:#aaa;letter-spacing:.3px}
.social{top:1154px;width:23px;height:23px;background:#111;border:1px solid #444}
</style>
</head>
<body>

<header class="site-header abs">
  <div class="brand abs">CARGOLINX</div>
  <div class="brand-tag abs">A DIVERSIFIED FREIGHT COMPANY</div>
  <nav class="main-nav">
    <a class="active" style="left:335px">HOME</a>
    <a style="left:404px">SERVICES</a>
    <a style="left:480px">INSURANCE</a>
    <a style="left:566px">LEGAL INFO</a>
    <a style="left:655px">CONTACT</a>
  </nav>
  <div class="btn-reserve abs">
    <svg width="10" height="10" viewBox="0 0 10 10"><rect x=".5" y="1.5" width="9" height="8" fill="none" stroke="#fff"/><rect x=".5" y="1.5" width="9" height="2" fill="#fff"/><rect x="3" y="5" width="2" height="2" fill="#fff"/></svg>
    RESERVATION
  </div>
</header>

<section class="hero abs" role="img" aria-label="Container ship loaded with stacked cargo containers under port cranes"></section>
<div class="hero-caption abs">
  <h1>GET FAST &amp; FREE FREIGHT QUOTES</h1>
  <p>WORLDWIDE SHIPPING- OCEAN AND TRUCKING WITH NO LIMITS</p>
</div>
<div class="slider-arrow abs" style="left:90px"><svg width="8" height="12" viewBox="0 0 8 12"><path d="M6 1 1 6l5 5" fill="none" stroke="#bbb" stroke-width="2"/></svg></div>
<div class="slider-arrow abs" style="left:853px"><svg width="8" height="12" viewBox="0 0 8 12"><path d="M2 1l5 5-5 5" fill="none" stroke="#bbb" stroke-width="2"/></svg></div>

<main class="content-panel abs"></main>

<article class="service-card abs" style="left:112px">
  <div class="thumb" role="img" aria-label="Heavy haul truck with large equipment tires" style="background:linear-gradient(90deg,#8a6a3a,#b43a36,#6f4a3c)"></div>
  <div class="bar"><h3>HEAVY HAUL SERVICES</h3><span>View Details +</span></div>
</article>
<article class="service-card abs" style="left:371px">
  <div class="thumb" role="img" aria-label="White refrigerated truck on the highway" style="background:linear-gradient(90deg,#6d7a5a,#e9ecef,#9fb0be)"></div>
  <div class="bar"><h3>DRY &amp; REFRIGERATED SERVICES</h3><span>View Details +</span></div>
</article>
<article class="service-card abs" style="left:628px">
  <div class="thumb" role="img" aria-label="Container ship at sea" style="background:linear-gradient(180deg,#9bb6cc,#3a64a0 60%,#2a4a6a)"></div>
  <div class="bar"><h3>FREIGHT FORWARDINGOCEAN SERVICES</h3><span>View Details +</span></div>
</article>

<h2 class="section-title abs" style="left:112px;top:553px;color:var(--blue);font-weight:400">INTERNATIONAL EXPERIENCE. LOCAL EXPERTISE</h2>
<div class="rule abs" style="left:112px;top:572px;width:493px"></div>

<div class="intro-photo abs" role="img" aria-label="Air cargo aircraft fuselage at the loading dock"></div>
<div class="intro-copy abs">
  <p>Welcome to CargoLinx and Linx Logistics Inc. We are a one stop solution logistics company servicing Worldwide with our Trucking and Ocean shipping service. In using our freight services, we will negotiate a competitive freight quote using over 5000 different carriers who are certified and contracted by us. We have all equipment types available daily, service all freight types, and have no limits Worldwide.</p>
  <p>Whether you need a freight quote for a full load, LTL/Partial load, or Oversized Machinery or Equipment, trucking and/or ocean shipment, we will take care of it. All your freight or equipment to be shipped will be covered in full by our insurance</p>
</div>
<p class="cta abs">Get your freight quote online now or call 888-555-0142 now and let some of the top carriers in the country compete for your business</p>

<h2 class="section-title abs" style="left:629px;top:555px;color:#666;font-weight:400">SIDE BAR MENU</h2>
<div class="rule abs" style="left:629px;top:573px;width:235px"></div>
<aside class="sidebar abs" style="left:650px;top:593px">
  <h4>WORLDWIDE FREIGHT SERVICES</h4>
  <ul><li>Worldwide Shipping Scope</li><li>Trucking Shipping Services</li><li>Ocean Shipping Services</li><li>Insurance &amp; Legal Details</li></ul>
  <h4>FREIGHT - TRUCKING SERVICE</h4>
  <ul><li>Heavy Equipment Hauling</li><li>LTL Freight Transport</li><li>Flatbed Transport</li><li>Step Deck Transport</li><li>Dry Van Transport</li><li>Refrigerated Transport</li><li>Power Only &amp; Towaway Transport</li></ul>
</aside>

<section class="newsletter abs">
  <label>Sign up for Newsletter:</label>
  <div class="field">Enter your email Address....</div>
  <div class="submit">SUBMIT</div>
</section>

<footer class="site-footer abs">
  <h5 style="left:112px">QUICK CONTACT</h5>
  <h5 style="left:306px">SITE LINKS</h5>
  <ul class="contact-list abs">
    <li><svg viewBox="0 0 8 10"><path d="M4 0a3 3 0 0 0-3 3c0 2.5 3 7 3 7s3-4.5 3-7a3 3 0 0 0-3-3zm0 4.2A1.2 1.2 0 1 1 4 1.8a1.2 1.2 0 0 1 0 2.4z" fill="#fff"/></svg>220 HARBOUR ROW, SUITE 410</li>
    <li><span style="width:8px"></span>KINGSPORT, ON, K0A 1B0, CANADA</li>
    <li><svg viewBox="0 0 8 10"><rect x="1.5" y=".5" width="5" height="9" rx="1" fill="none" stroke="#fff"/></svg>CALL US: <span style="color:#fff">+1 555-010-2400</span></li>
    <li><svg viewBox="0 0 8 10"><rect x="0" y="2" width="8" height="6" fill="#fff"/><path d="M0 2l4 3 4-3" fill="none" stroke="#262626"/></svg><span style="color:#fff">INFO@CARGOLINX.COM</span></li>
  </ul>
  <ul class="link-col abs" style="left:308px;top:64px"><li>HOME</li><li>ABOUT US</li><li>SERVICES</li><li>MEDIA</li></ul>
  <ul class="link-col abs" style="left:501px;top:64px"><li>LINKS ONE</li><li>LINKS ONE</li><li>LINKS ONE</li><li>LINKS ONE</li></ul>
</footer>
<div class="footer-rule abs"></div>
<p class="footer-note abs">Full Loads, LTL, Oversized Machinery &amp; Equipment.<br>We do it all. All freight covered to full value by our Insurance!</p>
<span class="social-label abs">GET SOCIAL</span>
<div class="social abs" style="left:785px"></div>
<div class="social abs" style="left:814px"></div>
<div class="social abs" style="left:843px"></div>

</body>
</html>
```